Redesign for Real Estate Lead Generation Site

We are looking for a slight redesign for our real estate lead generation sites.

Here's one of our current sites: www.lbrhousetrends.net

The design should be simple as it is currently, remain only on one page, and nothing too detailed to where it may take a while to load/reload. We also have parallel sites, www.gkmhousetrends.net, www.gkmquickdeals.net, and a few others which all will end up utilizing the same template.

We've found that the majority of the site traffic will come from print advertising, not as much SEO. But also understand the more simple the site, the greater likelihood a user may find us through search engines. Another reason we want to keep it rather simple and clean.

The content on the page needs to remain the same, but with additional spaces for one written paragraph testimonial, and an area where we can incorporate a video. Originally, the ideal spot would be the open white space below the social media logos, but we are open to different ideas as you create the redesign.

A change in colors and simple graphics is what we're looking for most along with the testimonial / video additions. Also, we have a new logo we need incorporated into the site somewhere: http://www.bertoprintworks.net/MV-Crew-Estates.zip to download the file in different formates.

Here is our main site, www.mvcrewestates.net through wordpress, so you can get an idea of what folks go to once they've signed up and received a confirm e-mail.

Please contact us if you have any questions. Good luck and thanks for submitting!

```html
<!DOCTYPE html>
<html lang="en">
<head>
<meta charset="utf-8">
<title>MV Crew Estates – Home Value Report</title>
<link href="https://fonts.googleapis.com/css2?family=Arimo:ital,wght@0,400;0,700;1,400&family=Ubuntu:wght@400&display=swap" rel="stylesheet">
<style>
:root{
  --page:#ebebeb;
  --header:#f7f7f7;
  --band-grey:#7b8790;
  --orange:#f9a51a;
  --orange-dark:#f39312;
  --ink:#333;
  --ink-soft:#555;
  --field-border:#c9c9c9;
  --field-bg:#fbfbfb;
  --blue:#1f6ec5;
  --blue-dark:#0e4d99;
  --footer:#2a2a2a;
  --white:#fff;
  --photo-tone:#9b6a5f;
  --video-tone:#8a7d66;
}
*{box-sizing:border-box;margin:0;padding:0}
html,body{width:909px;height:1200px;overflow:hidden}
body{position:relative;background:var(--page);font-family:Arimo,Arial,sans-serif;color:var(--ink)}
.site-header{position:absolute;left:0;top:0;width:909px;height:123px;background:var(--header)}
.brand{position:absolute;left:36px;top:22px;display:flex;align-items:center;gap:10px}
.brand-mark{width:68px;height:78px;background:var(--ink)}
.brand-name{font-size:26px;line-height:28px;color:var(--ink)}
.phone{position:absolute;right:28px;top:26px;display:flex;align-items:center;gap:12px;font-size:22px;color:var(--ink)}
.grey-band{position:absolute;left:0;top:123px;width:909px;height:19px;background:var(--band-grey)}
.headline-band{position:absolute;left:0;top:142px;width:909px;height:74px;
  background:linear-gradient(var(--orange),var(--orange-dark));box-shadow:0 2px 3px rgba(0,0,0,.25);
  display:flex;align-items:center;justify-content:center}
.headline-band h1{font-family:Ubuntu,sans-serif;font-weight:400;font-size:21px;color:var(--white);text-shadow:0 1px 1px rgba(0,0,0,.25)}
.form-card{position:absolute;left:36px;top:249px;width:447px;height:536px;background:var(--white);box-shadow:0 1px 4px rgba(0,0,0,.2)}
.intro{position:absolute;left:18px;top:18px;width:410px;font-size:12.5px;line-height:19px}
.field{position:absolute;height:32px;border:1px solid var(--field-border);background:var(--field-bg);font-size:12.5px;color:var(--ink-soft);padding:9px 7px;line-height:14px}
.label{position:absolute;font-size:12.5px;color:var(--ink-soft);line-height:14px}
.select{display:flex;justify-content:space-between;padding-right:4px}
.segmented{position:absolute;left:89px;top:255px;width:338px;height:31px;border:1px solid var(--field-border);display:flex;font-size:12.5px;color:var(--ink-soft)}
.segmented span{flex:1;display:flex;align-items:center;justify-content:center}
.segmented .active{flex:0 0 72px;background:#ededed;border-right:1px solid var(--field-border)}
.comments{height:102px}
.note{position:absolute;left:18px;top:411px;width:420px;font-size:10px;line-height:14px}
.submit{position:absolute;left:148px;top:461px;width:135px;height:54px;border-radius:4px;
  background:linear-gradient(var(--blue),var(--blue-dark));border:1px solid #0c3f80;
  color:var(--white);font:700 28px Arimo,Arial,sans-serif;display:flex;align-items:center;justify-content:center}
.house-photo{position:absolute;left:517px;top:251px;width:356px;height:536px;background:var(--photo-tone);box-shadow:2px 3px 4px rgba(0,0,0,.3)}
.testimonial{position:absolute;left:55px;top:827px;width:800px;font-size:10px;line-height:19px}
.testimonial cite{display:block;font-size:12.5px;font-style:italic}
.video{position:absolute;left:35px;top:914px;width:267px;height:178px;background:#fff;border:1px solid #ccc}
.video-frame{width:100%;height:150px;background:var(--video-tone)}
.video-bar{height:27px;display:flex;align-items:center;gap:8px;padding:0 8px;font-size:10px;color:var(--ink-soft);border-top:4px solid #d33}
.about{position:absolute;left:321px;top:909px;width:555px;font-size:12.5px;line-height:19px}
.about p{margin-bottom:23px}
.site-footer{position:absolute;left:0;top:1124px;width:909px;height:76px;background:var(--footer);color:var(--white);font-size:12.5px}
.copyright{position:absolute;left:36px;top:30px}
.social{position:absolute;right:36px;top:19px;display:flex;align-items:center;gap:22px}
.social i{display:block;width:27px;height:27px;border-radius:3px;background:#4a7fc0}
</style>
</head>
<body>
<header class="site-header">
  <div class="brand"><div class="brand-mark"></div><div class="brand-name">MV Crew<br>Estates</div></div>
  <div class="phone">
    <svg width="30" height="24" viewBox="0 0 30 24"><path d="M2 8c0-6 26-6 26 0v3h-7V8H9v3H2z" fill="#333"/><rect x="6" y="12" width="18" height="11" rx="2" fill="#333"/><circle cx="15" cy="17" r="3" fill="#f7f7f7"/></svg>
    <span>555-014-2287</span>
  </div>
</header>
<div class="grey-band"></div>
<div class="headline-band"><h1>"What is the current market value of my home in today's market?"</h1></div>

<section class="form-card">
  <p class="intro">Fill out the form below for a FREE Comparative Market Analysis Report from MV Crew Estates for an estimate of your home's current value.</p>
  <div class="field" style="left:18px;top:69px;width:197px">Your Name</div>
  <div class="field" style="left:232px;top:69px;width:197px">Email Address</div>
  <div class="field" style="left:18px;top:114px;width:197px">Phone Number</div>
  <div class="field" style="left:232px;top:114px;width:197px">Street Address</div>
  <div class="field" style="left:18px;top:162px;width:197px">City</div>
  <div class="field" style="left:232px;top:162px;width:127px">ZIP</div>
  <div class="field select" style="left:374px;top:162px;width:55px"><span>State</span><span>▾</span></div>
  <span class="label" style="left:25px;top:218px">Number of Bedrooms</span>
  <div class="field" style="left:161px;top:209px;width:55px"></div>
  <span class="label" style="left:236px;top:218px">Number of Bathrooms</span>
  <div class="field" style="left:374px;top:209px;width:55px"></div>
  <span class="label" style="left:19px;top:264px">Conditions</span>
  <div class="segmented"><span class="active">Excellent</span><span>Good</span><span>Average</span><span>Poor</span></div>
  <div class="field comments" style="left:18px;top:300px;width:411px">Addtional Comments</div>
  <p class="note">*The more complete the form the easier it will be to provide an accurate report regarding the value of your home.</p>
  <div class="submit">SUBMIT</div>
</section>

<div class="house-photo" role="img" aria-label="Photo of a two-storey brick family home"></div>

<blockquote class="testimonial">
  "If a highly insightful, proactive and detailed oriented Real Estate agent is what you seek, look no further! Marcus comes with a deep knowledge base of the market and a dedicated eye for a great deal which only adds to the many attributes he has to offer. I will never use another agent again; you shouldn't either!"
  <cite>— Dana Whitfield</cite>
</blockquote>

<div class="video">
  <div class="video-frame" role="img" aria-label="Video introducing the real estate team"></div>
  <div class="video-bar"><span>▶</span><span>0:00 / 0:00</span></div>
</div>

<div class="about">
  <p>Whether you are moving to, from or within the Metro Washington area, you need a certified professional for your next move.</p>
  <p>A certified professional such as Marcus Vance and his team can literally save you thousands on your next real estate transaction. Put his knowledge to work today!</p>
  <p>The Marcus Vance Real Estate Team is in TOP 1% of all Crestline agents worldwide.</p>
  <p>We are a Pinnacle Producer selling over 85 million in Real Estate HCAR and SAR Member CCRD Designate (Commercial Designation) LBG member (Land Brokers Guild).</p>
</div>

<footer class="site-footer">
  <span class="copyright">© 2010 MV Crew Estates</span>
  <div class="social"><span>Join the Discussion</span><i></i><i style="background:#39a9d6"></i><i style="background:#c8322a"></i></div>
</footer>
</body>
</html>
```